Company Website

We require an online clothing store website for construction workwear.
It needs to be easy to read, user friendly, easy to navigate purchasing.
We are after designs incorporating our recently design logo, and colour combinations black white and orange (same as the company logo). Needs to highlight quality, safety and products. Any ideas around highlighting branding are welcome.

Target Market(s)

Construction workers and businesses.

Industry/Entity Type

Construction

Coding

Coded - Design and coding required

Number of Pages Required

5+ page

Colors
EE7325
F08F49
F5BC92
FAE3D3
FDF4ED

Requirements
Must have
• Include all pictures, prices and details of the products we sell. See PDF uploaded to brief.
Nice to have
• Simple access to purchase items. Easy to navigate website layout.

```html
<!DOCTYPE html>
<html lang="en">
<head>
<meta charset="utf-8">
<title>Guardline Workwear</title>
<link href="https://fonts.googleapis.com/css2?family=Michroma&family=Roboto:wght@400;500;700&family=Open+Sans:wght@400;600&display=swap" rel="stylesheet">
<style>
:root{
  --orange:#f05a0a;
  --orange-soft:#EE7325;
  --peach:#F5BC92;
  --cream:#FDF4ED;
  --black:#000;
  --ink:#111;
  --grey:#666;
  --line:#e6e6e6;
  --white:#fff;
}
*{box-sizing:border-box;margin:0;padding:0}
html,body{width:1200px;height:3769px;overflow:hidden}
body{position:relative;background:var(--white);font-family:"Roboto",sans-serif;color:var(--ink)}
.abs{position:absolute}
.display{font-family:"Michroma",sans-serif;text-transform:uppercase}

/* top bar */
.topbar{left:0;top:0;width:1200px;height:46px;background:var(--orange);display:flex;align-items:center;justify-content:center;gap:28px;color:#fff;font-size:13px}
.topbar .btn{background:#000;color:#fff;padding:7px 18px;font-size:13px}

/* header */
.brand{font-family:"Michroma",sans-serif;color:var(--orange);font-size:30px;line-height:1;letter-spacing:1px}
.brand small{display:block;font-size:12px;letter-spacing:9px;margin-top:6px;text-align:right}
.nav{top:104px;display:flex;font-size:13px;font-weight:500}
.nav a{position:absolute;white-space:nowrap;color:var(--ink);text-decoration:none}
.nav a.active{color:var(--orange)}
.icon-btn{width:30px;height:30px;border-radius:50%;background:#000;display:flex;align-items:center;justify-content:center}

/* hero */
.hero{left:0;top:186px;width:1200px;height:592px;background:linear-gradient(90deg,#3a3a3a 0%,#3a3a3a 42%,#6b5a48 60%,#c98a3e 75%,#a8a58c 100%)}
.hero .welcome{left:105px;top:150px;color:#fff;font-size:22px}
.hero .name{left:105px;top:196px;color:#fff;font-size:54px;letter-spacing:2px;line-height:1}
.hero .name small{display:block;font-size:19px;letter-spacing:14px;margin-top:10px;text-align:right}
.hero p{left:105px;top:302px;width:460px;color:#fff;font-size:18px;line-height:34px;font-weight:500}
.btn-orange{background:var(--orange);color:#fff;font-weight:700;font-size:17px;display:flex;align-items:center;justify-content:center}
.btn-outline{border:2px solid #fff;color:#fff;font-weight:700;font-size:17px;display:flex;align-items:center;justify-content:center}
.arrow-circle{width:34px;height:34px;border:1.5px solid #fff;border-radius:50%;display:flex;align-items:center;justify-content:center}

/* sections */
.section-title{font-size:34px;line-height:1;color:#000}
.rule{height:2px;width:66px;background:var(--peach)}

/* filter */
.search{left:111px;top:944px;width:223px;height:39px;background:var(--orange);color:#fff;font-size:13px;display:flex;align-items:center;justify-content:space-between;padding:0 22px}
.cat{left:111px;width:223px;height:40px;background:#000;color:#fff;font-weight:700;font-size:15px;display:flex;align-items:center;justify-content:space-between;padding:0 22px}
.sub{left:134px;font-family:"Open Sans",sans-serif;font-size:12px;color:#555}

/* products */
.card{width:205px;height:322px;border:1px solid var(--line);background:#fff;text-align:center}
.card .photo{position:absolute;left:10px;top:12px;width:183px;height:180px}
.card h3{position:absolute;left:0;right:0;top:210px;font-size:13.5px;font-weight:500;line-height:24px;text-transform:uppercase}
.card .price{position:absolute;left:0;right:0;font-size:17px;font-weight:700;color:var(--orange)}
.card .view{position:absolute;left:50%;transform:translateX(-50%);width:104px;height:32px;background:#000;color:#fff;font-size:11.5px;font-weight:700;display:flex;align-items:center;justify-content:center}

/* service band */
.band{left:0;top:2139px;width:1200px;height:214px;background:linear-gradient(100deg,#f0560a 0%,#e24e06 50%,#f36a1c 100%)}
.feature{color:#fff;font-family:"Open Sans",sans-serif;font-size:21px}

/* testimonials */
.quote-card{width:475px;height:278px;background:#fff;box-shadow:0 4px 22px rgba(0,0,0,.08);border-radius:6px;font-family:"Open Sans",sans-serif}
.quote-card .mark{position:absolute;left:40px;top:60px;font-family:Georgia,serif;font-size:90px;line-height:1;color:var(--peach)}
.quote-card p{position:absolute;left:40px;top:108px;width:400px;font-size:13px;line-height:30px;color:#555}
.quote-card .who{position:absolute;left:40px;top:210px;font-size:13px;color:#777}
.quote-card .who b{color:var(--orange);font-weight:600}

/* banner */
.footer{left:0;top:3109px;width:1200px;height:660px;background:#000}
.banner{left:123px;top:2878px;width:879px;height:377px;border-radius:16px;background:linear-gradient(90deg,#8fb126 0%,#3f5a2a 25%,#c8d62a 45%,#2f3f6a 60%,#b7c82a 75%,#2a2a2a 100%)}
.banner .shade{position:absolute;inset:0;border-radius:16px;background:rgba(0,0,0,.25)}
.banner h2{position:absolute;left:0;right:0;top:104px;text-align:center;color:#fff;font-size:48px}
.banner p{position:absolute;left:0;right:0;top:170px;text-align:center;color:#fff;font-size:17px;font-weight:500}

/* footer */
.foot-head{font-size:21px;color:var(--orange)}
.foot-rule{height:2px;width:50px;background:var(--orange)}
.foot-links{list-style:none;color:#fff;font-size:14.5px;line-height:30px}
.pay{width:66px;height:40px;background:#fff;border-radius:4px;display:flex;align-items:center;justify-content:center;font-size:9.5px;font-weight:700;color:#1a1a1a;text-align:center;line-height:1.1}
</style>
</head>
<body>

<!-- Top bar -->
<div class="abs topbar"><span>"Lorem ipsum dolor sit amet, consectetur adipiscing elit</span><span class="btn">Shop Now</span></div>

<!-- Header -->
<div class="abs brand" style="left:111px;top:90px">GUARDLINE<small>WORKWEAR</small></div>
<nav class="abs nav" style="left:0;width:1200px">
  <a class="active" style="left:512px">Home</a>
  <a style="left:587px">Shop</a>
  <a style="left:657px">Products</a>
  <a style="left:749px">Blog</a>
  <a style="left:816px">FAQS</a>
  <a style="left:888px">Contact Us</a>
</nav>
<div class="abs icon-btn" style="left:979px;top:98px"><svg width="14" height="14" viewBox="0 0 14 14"><circle cx="6" cy="6" r="4.5" stroke="#fff" stroke-width="2" fill="none"/><line x1="9.5" y1="9.5" x2="13" y2="13" stroke="#fff" stroke-width="2"/></svg></div>
<div class="abs icon-btn" style="left:1018px;top:98px"><svg width="16" height="16" viewBox="0 0 16 16"><circle cx="8" cy="5" r="3.2" stroke="#fff" stroke-width="1.6" fill="none"/><path d="M2 15c0-3.5 2.7-5.5 6-5.5s6 2 6 5.5" stroke="#fff" stroke-width="1.6" fill="none"/></svg></div>
<div class="abs icon-btn" style="left:1057px;top:98px"><svg width="16" height="16" viewBox="0 0 16 16"><path d="M1 2h2.5l2 8h8l1.5-6H4.5" stroke="#fff" stroke-width="1.6" fill="none"/><circle cx="6.5" cy="13" r="1.3" fill="#fff"/><circle cx="12.5" cy="13" r="1.3" fill="#fff"/></svg></div>
<div class="abs" style="left:1075px;top:96px;width:12px;height:12px;border-radius:50%;background:var(--orange);color:#fff;font-size:8px;display:flex;align-items:center;justify-content:center">0</div>

<!-- Hero -->
<section class="abs hero" role="img" aria-label="Site worker in hi-vis orange vest and hard hat reviewing a clipboard on a construction site">
  <div class="abs display welcome">Welcome to</div>
  <div class="abs display name">GUARDLINE<small>WORKWEAR</small></div>
  <p class="abs">Sed ut perspiciatis unde omnis iste natus error sit voluptatem accusantium.</p>
  <div class="abs btn-orange" style="left:105px;top:391px;width:188px;height:46px">ORDER ONLINE</div>
  <div class="abs btn-outline" style="left:307px;top:391px;width:249px;height:46px">VIEW COLLECTIONS</div>
  <div class="abs arrow-circle" style="left:36px;top:280px"><svg width="10" height="10" viewBox="0 0 10 10"><path d="M6.5 1.5L3 5l3.5 3.5" stroke="#fff" stroke-width="1.5" fill="none"/></svg></div>
  <div class="abs arrow-circle" style="left:1126px;top:280px;border-color:rgba(255,255,255,.5)"><svg width="10" height="10" viewBox="0 0 10 10"><path d="M3.5 1.5L7 5 3.5 8.5" stroke="#fff" stroke-width="1.5" fill="none"/></svg></div>
</section>

<!-- Filter -->
<h2 class="abs display section-title" style="left:111px;top:853px">Filter</h2>
<div class="abs rule" style="left:111px;top:902px"></div>
<div class="abs search"><span>Search Here</span><svg width="12" height="12" viewBox="0 0 14 14"><circle cx="6" cy="6" r="4.5" stroke="#fff" stroke-width="2" fill="none"/><line x1="9.5" y1="9.5" x2="13" y2="13" stroke="#fff" stroke-width="2"/></svg></div>
<div class="abs cat" style="top:1007px">All Categories<span>&#8964;</span></div>
<div class="abs cat" style="top:1061px">Men's Shirt<span>&#8963;</span></div>
<div class="abs sub" style="top:1123px">Shirt</div>
<div class="abs sub" style="top:1152px">Jumper</div>
<div class="abs sub" style="top:1181px">Vest</div>
<div class="abs sub" style="top:1211px">Pants</div>
<div class="abs cat" style="top:1252px">Men's Pants<span>&#8964;</span></div>
<div class="abs cat" style="top:1307px">Women's Shirt<span>&#8964;</span></div>
<div class="abs cat" style="top:1361px">Women's Pants<span>&#8964;</span></div>
<div class="abs cat" style="top:1416px">Other<span>&#8964;</span></div>

<!-- Featured products -->
<h2 class="abs display section-title" style="left:395px;width:692px;text-align:center;top:853px">Featured Products</h2>
<div class="abs rule" style="left:690px;width:100px;top:902px"></div>

<div class="abs card" style="left:395px;top:947px">
  <div class="photo" role="img" aria-label="Orange long-sleeve vented work shirt with reflective tape" style="background:radial-gradient(ellipse at center,#f36b1c 0 48%,#fff 50%)"></div>
  <h3>Mens L/S Standard<br>Vented Orange Shirt</h3><div class="price" style="top:266px">$43.95EA</div><div class="view" style="top:306px">VIEW DETAILS</div>
</div>
<div class="abs card" style="left:639px;top:947px">
  <div class="photo" role="img" aria-label="Two-toned orange/navy and yellow/navy taped work shirts" style="background:linear-gradient(90deg,#fff 0,#f0801e 15%,#2b3a66 45%,#f2e21a 60%,#2b3a66 88%,#fff 100%)"></div>
  <h3>Mens L/S Two-Toned<br>Vented Taped Shirt</h3><div class="price" style="top:266px">$43.95EA</div><div class="view" style="top:306px">VIEW DETAILS</div>
</div>
<div class="abs card" style="left:882px;top:947px">
  <div class="photo" role="img" aria-label="Orange long-sleeve reflective work shirt" style="background:radial-gradient(ellipse at center,#ef7a2c 0 48%,#fff 50%)"></div>
  <h3>Mens L/S Reflective<br>Vented Orange Shirt</h3><div class="price" style="top:266px">$44.95EA</div><div class="view" style="top:306px">VIEW DETAILS</div>
</div>

<div class="abs card" style="left:395px;top:1326px">
  <div class="photo" role="img" aria-label="Hi-vis lime and orange long-sleeve polos with navy lower panel" style="background:linear-gradient(180deg,#fff 0,#c9f23a 20%,#f07a1c 45%,#1f2a48 70%,#fff 100%)"></div>
  <h3 style="top:210px">Hi- Vis L/S Polo</h3><div class="price" style="top:240px">$23.00EA</div><div class="view" style="top:280px">VIEW DETAILS</div>
</div>
<div class="abs card" style="left:639px;top:1326px">
  <div class="photo" role="img" aria-label="Hi-vis orange and lime short-sleeve polos with navy lower panel" style="background:linear-gradient(180deg,#fff 0,#f07a1c 25%,#c4f03a 50%,#1a1a1a 75%,#fff 100%)"></div>
  <h3 style="top:210px">Hi-Vis S/S Polo</h3><div class="price" style="top:240px">$18.95EA</div><div class="view" style="top:280px">VIEW DETAILS</div>
</div>
<div class="abs card" style="left:882px;top:1326px">
  <div class="photo" role="img" aria-label="Navy work pants with reflective bands" style="background:linear-gradient(90deg,#fff 0 35%,#1e2a55 36% 64%,#fff 65%)"></div>
  <h3 style="top:210px">Hi-Vis Navy Pants</h3><div class="price" style="top:240px">$45.00EA</div><div class="view" style="top:280px">VIEW DETAILS</div>
</div>

<div class="abs card" style="left:395px;top:1704px">
  <div class="photo" role="img" aria-label="Orange long-sleeve shirt with double reflective hoop" style="background:radial-gradient(ellipse at center,#f36b1c 0 48%,#fff 50%)"></div>
  <h3>Hi-Vis Navy Pants -<br>Double Hoop</h3><div class="price" style="top:266px">$47.00EA</div><div class="view" style="top:306px">VIEW DETAILS</div>
</div>

<!-- Service band -->
<section class="abs band">
  <svg class="abs" style="left:111px;top:56px" width="62" height="40" viewBox="0 0 62 40"><rect x="2" y="6" width="36" height="24" rx="3" fill="#fff"/><path d="M38 12h12l9 10v8H38z" fill="#fff"/><circle cx="14" cy="32" r="6" fill="#fff" stroke="#f05a0a" stroke-width="3"/><circle cx="48" cy="32" r="6" fill="#fff" stroke="#f05a0a" stroke-width="3"/></svg>
  <svg class="abs" style="left:358px;top:56px" width="42" height="42" viewBox="0 0 42 42"><circle cx="21" cy="21" r="14" stroke="#fff" stroke-width="3" fill="none"/><rect x="3" y="16" width="7" height="12" rx="2" fill="#fff"/><rect x="32" y="16" width="7" height="12" rx="2" fill="#fff"/><text x="21" y="25" text-anchor="middle" fill="#fff" font-size="9" font-family="Roboto" font-weight="700">24/7</text></svg>
  <svg class="abs" style="left:676px;top:56px" width="40" height="42" viewBox="0 0 40 42"><circle cx="20" cy="13" r="9" fill="#fff"/><path d="M4 40c0-10 7-15 16-15s16 5 16 15z" fill="#fff"/></svg>
  <svg class="abs" style="left:933px;top:56px" width="40" height="42" viewBox="0 0 40 42"><path d="M20 3l16 8v20L20 39 4 31V11z" stroke="#fff" stroke-width="3" fill="none"/><path d="M4 11l16 8 16-8M20 19v20" stroke="#fff" stroke-width="3" fill="none"/></svg>
  <div class="abs feature" style="left:111px;top:124px">Free Delivery</div>
  <div class="abs feature" style="left:358px;top:124px">Customer Care 24/7</div>
  <div class="abs feature" style="left:676px;top:124px">Support Care</div>
  <div class="abs feature" style="left:933px;top:124px">30 Days Return</div>
</section>

<!-- Testimonials -->
<h2 class="abs display section-title" style="left:102px;top:2420px">Our Happy Customers</h2>
<div class="abs rule" style="left:102px;top:2468px;width:110px"></div>
<svg class="abs" style="left:1057px;top:2440px" width="46" height="18" viewBox="0 0 46 18"><circle cx="8" cy="9" r="8" fill="#ccc"/><path d="M9.5 5.5L6 9l3.5 3.5" stroke="#fff" stroke-width="1.6" fill="none"/><circle cx="31" cy="9" r="8" fill="#000"/><path d="M29.5 5.5L33 9l-3.5 3.5" stroke="#fff" stroke-width="1.6" fill="none"/></svg>

<div class="abs quote-card" style="left:102px;top:2519px">
  <div class="mark">&ldquo;</div>
  <p>Lorem ipsum dolor sit amet, consectetur adipiscing elit, sed do eiusmod tempor incididunt ut labore et dolore magna aliqua. Quis ipsum suspendisse ultrices gravida.</p>
  <div class="who"><b>Daniel Reyes,</b> Lorem Lipsum</div>
</div>
<div class="abs quote-card" style="left:622px;top:2519px">
  <div class="mark">&ldquo;</div>
  <p>Lorem ipsum dolor sit amet, consectetur adipiscing elit, sed do eiusmod tempor incididunt ut labore et dolore magna aliqua. Quis ipsum suspendisse ultrices gravida.</p>
  <div class="who"><b>Daniel Reyes,</b> Lorem Lipsum</div>
</div>

<!-- Footer -->
<footer class="abs footer"></footer>

<section class="abs banner" role="img" aria-label="Rack of hi-vis yellow, orange and navy workwear jackets">
  <div class="shade"></div>
  <h2 class="display">Be Seen. Be Safe.</h2>
  <p>Lorem Ipsum is simply dummy text of the printing and typesettin</p>
  <div class="abs btn-orange" style="left:401px;top:223px;width:152px;height:45px">SHOP NOW</div>
</section>

<div class="abs brand" style="left:111px;top:3330px;font-size:24px">GUARDLINE<small style="font-size:9px;letter-spacing:7px;margin-top:4px">WORKWEAR</small></div>
<div class="abs" style="left:527px;top:3328px;width:365px;height:46px;background:#fff;font-family:'Open Sans',sans-serif;font-size:11px;color:#666;display:flex;align-items:center;padding-left:22px">Enter Email Address</div>
<div class="abs btn-orange" style="left:909px;top:3328px;width:178px;height:46px;font-size:15px">Subscribe Now</div>

<div class="abs" style="left:111px;top:3433px"><h4 class="display foot-head">Site Map</h4><div class="foot-rule" style="margin:12px 0 16px"></div><ul class="foot-links"><li>Home</li><li>Products</li><li>Reviews</li><li>Shop Now</li></ul></div>
<div class="abs" style="left:313px;top:3433px"><h4 class="display foot-head">Products</h4><div class="foot-rule" style="margin:12px 0 16px"></div><ul class="foot-links"><li>Work Wear</li><li>Shoes</li><li>Top</li><li>Bottom</li></ul></div>
<div class="abs" style="left:537px;top:3433px"><h4 class="display foot-head">Support</h4><div class="foot-rule" style="margin:12px 0 16px"></div><ul class="foot-links"><li>Customer Services</li><li>FAQ'S</li><li>Chat Live</li><li>Contact Us</li></ul></div>
<div class="abs" style="left:743px;top:3433px"><h4 class="display foot-head">Help</h4><div class="foot-rule" style="margin:12px 0 16px"></div><ul class="foot-links"><li>Terms Of Conditions</li><li>Privacy Policy</li><li>Return</li><li>Shipping</li></ul></div>
<div class="abs" style="left:936px;top:3433px"><h4 class="display foot-head">Follow Us</h4><div class="foot-rule" style="margin:12px 0 16px"></div><ul class="foot-links"><li>Friendbook</li><li>Chirper</li><li>Snapgram</li><li>Workline</li></ul></div>

<div class="abs" style="left:265px;top:3668px;display:flex;gap:20px">
  <div class="pay">Vexa</div><div class="pay">Meridian</div><div class="pay">OrchardPay</div><div class="pay">PayWell</div><div class="pay">Pavo Pay</div><div class="pay">Atlas Express</div><div class="pay">Quadra</div><div class="pay">Vendo</div>
</div>
<div class="abs" style="left:0;width:1200px;top:3738px;text-align:center;color:#fff;font-family:'Open Sans',sans-serif;font-size:10.5px">(C) Copyright 2024 | All Rights Reserved</div>

</body>
</html>
```